Allied Health team of Physiotherapists & Occupational Therapists seek a business card design

We have our new logo, we now need our new business cards and stationary. Blossom: Lymphoedema & Women's Clinic is seeking a generic card design to represent our whole team and individual cards for each therapist that incorporates our new logo to communicate our holistic approach that is calming, nuturing, supportive and welcoming.
Our Physiotherapists and Occupational Therapists assess, treat and provide education for people who are at risk of or who have lymphoedema. This is often as a result of treatment for cancer. We provide pre-operative and post-operative management and cancer rehabilitation in our Pilates studio. Our team also consists of Physiotherapists who have a strong interest in pelvic floor and continence management for both men and women.

Target Market(s)

Mainly women health conscious

Industry/Entity Type

Allied Health: Physiotherapy / Occupational Therapy

Contact Information for Business Card

Address: 14 Calloway Ave Frankston 3199 Phone: 84317560 fax: 8431 7564 Email: info@blossomcarepartners.com.au Website: blossomcarepartners.com.au Facebook address: facebook.com/BlossomLymphoedemaAndWomensCareCentre. Room to write appointments. Individual cards need to have name, office email and individual email and professional details

Requirements
Must have
• Logo as per uploaded documents

```html
<!DOCTYPE html>
<html lang="en">
<head>
<meta charset="utf-8">
<title>Blossom – Business Card</title>
<link href="https://fonts.googleapis.com/css2?family=Montserrat:wght@400;500&display=swap" rel="stylesheet">
<style>
  :root {
    --backdrop: #3b4550;
    --card-white: #ffffff;
    --peach: #f4b08f;
    --peach-soft: #f8cdb5;
    --sage: #a3ad9f;
    --sage-soft: #c3cabf;
    --slate-text: #8f9891;
  }
  html, body {
    margin: 0;
    width: 1200px;
    height: 947px;
    overflow: hidden;
    background: var(--backdrop);
    font-family: "Montserrat", sans-serif;
  }
  .stage {
    position: relative;
    width: 1200px;
    height: 947px;
  }
  .card {
    position: absolute;
    top: 330px;
    width: 500px;
    height: 286px;
    border-radius: 4px;
    box-shadow: 0 12px 30px rgba(0,0,0,.35);
    overflow: hidden;
  }
  .card-front { left: 70px; background: var(--card-white); }
  .card-back { left: 630px; background: var(--peach); }

  .leaf-arc {
    position: absolute;
    right: 22px;
    top: 30px;
    width: 200px;
    height: 130px;
    border-radius: 200px 200px 0 0;
    background: linear-gradient(135deg, var(--sage-soft) 0%, var(--peach-soft) 100%);
    opacity: .55;
  }

  .brand {
    position: absolute;
    display: flex;
    align-items: center;
    gap: 10px;
    font-weight: 500;
    letter-spacing: .02em;
    white-space: nowrap;
  }
  .brand-dot {
    width: 12px;
    height: 12px;
    border-radius: 50%;
  }
  .card-front .brand {
    left: 30px;
    top: 112px;
    font-size: 28px;
    color: var(--peach);
  }
  .card-front .brand-dot { background: var(--peach); }

  .card-back .brand {
    left: 50%;
    top: 50%;
    transform: translate(-50%, -50%);
    font-size: 40px;
    color: var(--card-white);
  }
  .card-back .brand-dot { background: var(--card-white); }

  .person {
    position: absolute;
    left: 185px;
    bottom: 36px;
  }
  .person-name {
    margin: 0;
    font-size: 16px;
    font-weight: 500;
    color: var(--sage);
    letter-spacing: .02em;
    white-space: nowrap;
  }
  .person-role {
    margin: 2px 0 0;
    font-size: 13px;
    color: var(--peach);
  }
  .divider {
    position: absolute;
    left: 318px;
    bottom: 36px;
    width: 3px;
    height: 52px;
    background: var(--sage);
  }
  .contact {
    position: absolute;
    left: 332px;
    bottom: 38px;
    margin: 0;
    font-size: 10.5px;
    line-height: 1.6;
    color: var(--slate-text);
    font-style: normal;
    white-space: nowrap;
  }
</style>
</head>
<body>
<main class="stage">
  <section class="card card-front" aria-label="Business card front">
    <div class="leaf-arc" role="img" aria-label="Decorative arc of sage leaves with a peach curl"></div>
    <div class="brand"><span class="brand-dot"></span>Blossom</div>
    <div class="person">
      <p class="person-name">DANIEL HART</p>
      <p class="person-role">Founder</p>
    </div>
    <div class="divider"></div>
    <address class="contact">
      T: 987-654-321<br>
      E: info@blossomclinic.com<br>
      W: www.blossomclinic.com
    </address>
  </section>

  <section class="card card-back" aria-label="Business card back">
    <div class="brand"><span class="brand-dot"></span>Blossom</div>
  </section>
</main>
</body>
</html>
```